Shampoo and Conditioner label design

We have a shampoo and conditioner line that we're looking to re-brand. We need the label re-designed to have a more appealing look. I have uploaded our logo and an example of our current design. We're looking for a design that advertises a more natural & and organic feel w/ natural, cool colors. A great bench mark which we're trying to emulate is Baobab Dew. They have great packaging for their products and they are attractive to a lot of people.

Target Market(s)

Natural hair. Ethnic hair.

Industry/Entity Type

Hair Care Product

Logo Text

Lumi Bright Locks

Colors

Designer to choose colors to be used in the design.

Requirements
Must have
• Must describe what the product does for the individual making the purchase.
• - hydrating and moisturizing
• - improves healthy shine
• - strengthens hair
• - organic ingredients
• - Sulfate Free
• - Paraben Free
Nice to have
• an appealing design. welcoming with warm, natural colors. informative

```html
<!DOCTYPE html>
<html lang="en">
<head>
<meta charset="utf-8">
<title>Lumi Bright Locks – Label Series</title>
<link href="https://fonts.googleapis.com/css2?family=Roboto+Condensed:wght@300;400&display=swap" rel="stylesheet">
<style>
  :root{
    --paper:#ffffff;
    --olive:#7b8a2c;
    --leaf:#bcc562;
    --leaf-deep:#a9b84a;
    --cream:#f6f0d6;
    --butter:#ede3ab;
    --pale:#f2ecc4;
    --stone:#c3c3c5;
    --sky:#c9e3f3;
    --orange:#e1a031;
    --red:#c8312b;
    --ink:#222222;
    --grey:#555555;
    --silver:#9aa7b4;
    --stage-top:#efeee6;
    --stage-bottom:#aca77a;
  }
  *{box-sizing:border-box;margin:0;padding:0}
  html,body{width:1200px;height:1200px;overflow:hidden;background:var(--paper)}
  body{position:relative;font-family:"Roboto Condensed",Arial,sans-serif;font-weight:300}

  .label{position:absolute;width:210px;height:371px;overflow:hidden;border:1px solid #f1ebe0}
  .label__panel{position:absolute;inset:0}
  .label__panel--inset{inset:21px 17px 20px 18px}
  .label__content{position:absolute;inset:0}

  .brand{position:absolute;left:0;right:0;text-align:center;font-weight:400;font-size:21px;line-height:21px}
  .title{position:absolute;left:0;right:0;text-align:center;font-weight:300;font-size:23px;letter-spacing:.3px}
  .title--big{font-size:32px}
  .features{position:absolute;left:0;right:0;list-style:none;font-size:8.8px;line-height:12px;font-weight:400}
  .features li{white-space:nowrap}
  .features li:nth-child(1){padding-left:58px}
  .features li:nth-child(2){padding-left:42px}
  .features li:nth-child(3){padding-left:61px}
  .features li:nth-child(4){padding-left:36px}
  .features li:nth-child(5){padding-left:52px}
  .features li:nth-child(6){padding-left:36px}
  .features--loose{line-height:16px}
  .features--stagger li:nth-child(6){padding-left:68px}
  .hair-types{position:absolute;left:0;right:0;text-align:center;font-size:11px}
  .volume{position:absolute;left:0;right:0;text-align:center;font-size:8.5px;font-weight:400}

  /* 1 green conditioner */
  .label--green-cond{left:38px;top:194px;background:var(--paper)}
  .label--green-cond .label__panel{background:linear-gradient(90deg,var(--leaf) 0%,var(--leaf-deep) 60%,var(--leaf) 100%)}
  .label--green-cond .brand{top:78px;color:var(--grey)}
  .label--green-cond .title{top:160px;color:var(--paper)}
  .label--green-cond .features{top:203px;color:var(--ink)}
  .label--green-cond .hair-types{top:301px;color:var(--grey)}
  .label--green-cond .volume{top:337px;color:var(--grey)}

  /* 2 white conditioner */
  .label--white-cond{left:278px;top:194px;background:var(--paper)}
  .label--white-cond .label__panel{background:linear-gradient(180deg,#fbf6ea,#f7eed9)}
  .label--white-cond .brand{top:78px;color:var(--red)}
  .label--white-cond .title{top:160px;color:var(--red)}
  .label--white-cond .features{top:203px;color:var(--olive)}
  .label--white-cond .hair-types{top:300px;color:var(--red)}
  .label--white-cond .volume{top:337px;color:var(--red)}

  /* 3 grey/yellow conditioner */
  .label--stone-cond{left:511px;top:194px;background:var(--stone);border:none}
  .label--stone-cond .label__panel{background:var(--butter)}
  .label--stone-cond .side-band{position:absolute;left:0;top:0;width:24px;height:100%;background:#d6d6d4}
  .label--stone-cond .brand{top:78px;color:var(--silver)}
  .label--stone-cond .title{top:161px;color:var(--stone);font-weight:400}
  .label--stone-cond .features{top:201px;color:var(--olive);line-height:14.4px}
  .label--stone-cond .features span{background:var(--sky);padding:0 5px}
  .label--stone-cond .features li:nth-child(6){padding-left:60px}
  .label--stone-cond .hair-types{top:310px;color:var(--grey)}
  .label--stone-cond .volume{top:327px;color:var(--grey)}

  /* 4 orange shampoo */
  .label--orange-sham{left:38px;top:580px;background:var(--orange);border:none}
  .label--orange-sham .brand{top:54px;color:var(--grey)}
  .label--orange-sham .title{top:148px;color:var(--red)}
  .label--orange-sham .features{top:203px;color:var(--red)}
  .label--orange-sham .features li:nth-child(6){padding-left:68px}
  .label--orange-sham .hair-types{top:300px;color:var(--grey);font-size:13px}
  .label--orange-sham .volume{top:346px;color:var(--red)}

  /* 5 green/pale shampoo */
  .label--leaf-sham{left:278px;top:580px;background:var(--leaf);border:none}
  .label--leaf-sham .label__panel{background:linear-gradient(90deg,#efe8bb,#dcd98a)}
  .label--leaf-sham .brand{top:74px;color:var(--ink)}
  .label--leaf-sham .title{top:150px;color:var(--ink);font-size:30px}
  .label--leaf-sham .features{top:199px;color:var(--ink)}
  .label--leaf-sham .hair-types{top:300px;color:var(--orange)}
  .label--leaf-sham .volume{top:336px;color:var(--grey)}

  /* 6 white shampoo */
  .label--white-sham{left:511px;top:580px;background:var(--paper)}
  .label--white-sham .brand{top:68px;color:var(--red)}
  .label--white-sham .title{top:146px;color:var(--red)}
  .label--white-sham .features{top:202px;color:var(--olive);line-height:14.4px}
  .label--white-sham .hair-types{top:298px;color:var(--red)}
  .label--white-sham .volume{top:343px;color:var(--red)}

  /* presentation panel */
  .stage{position:absolute;left:756px;top:201px;width:402px;height:756px;background:linear-gradient(180deg,var(--stage-top),var(--stage-bottom))}
  .label--hero{left:92px;top:196px;width:218px;height:400px;background:var(--pale);border:none}
  .label--hero .brand{top:85px;color:var(--olive);font-size:24px;line-height:24px}
  .label--hero .title{top:178px;color:var(--red);font-size:25px;font-weight:400}
  .label--hero .features{top:225px;color:var(--olive);font-size:9.5px;line-height:15px}
  .label--hero .hair-types{top:330px;color:var(--red);font-size:13px;font-weight:400}
  .label--hero .volume{top:368px;color:var(--red);font-size:10px}
</style>
</head>
<body>

<section class="label label--green-cond">
  <div class="label__panel label__panel--inset" role="img" aria-label="Vertical wavy line pattern in green tones"></div>
  <div class="label__content">
    <div class="brand">Lumi Bright<br>Locks</div>
    <h2 class="title">CONDITIONER</h2>
    <ul class="features"><li>HYDRATING AND MOISTURIZING</li><li>IMPROVES HEALTHY SHINE</li><li>STRENGTHENS HAIR</li><li>ORGANIC INGREDIENTS</li><li>SULFATE FREE</li><li>PARABEN FREE</li></ul>
    <p class="hair-types">ALL HAIR TYPES</p>
    <p class="volume">16 Oz / 473 ml</p>
  </div>
</section>

<section class="label label--white-cond">
  <div class="label__panel label__panel--inset" role="img" aria-label="Faint cream wavy line pattern"></div>
  <div class="label__content">
    <div class="brand">Lumi Bright<br>Locks</div>
    <h2 class="title">CONDITIONER</h2>
    <ul class="features"><li>HYDRATING AND MOISTURIZING</li><li>IMPROVES HEALTHY SHINE</li><li>STRENGTHENS HAIR</li><li>ORGANIC INGREDIENTS</li><li>SULFATE FREE</li><li>PARABEN FREE</li></ul>
    <p class="hair-types">ALL HAIR TYPES</p>
    <p class="volume">16 Oz / 473 ml</p>
  </div>
</section>

<section class="label label--stone-cond">
  <div class="label__panel label__panel--inset"><div class="side-band"></div></div>
  <div class="label__content">
    <div class="brand">Lumi Bright<br>Locks</div>
    <h2 class="title">CONDITIONER</h2>
    <ul class="features"><li><span>HYDRATING AND MOISTURIZING</span></li><li><span>IMPROVES HEALTHY SHINE</span></li><li><span>STRENGTHENS HAIR</span></li><li><span>ORGANIC INGREDIENTS</span></li><li><span>SULFATE FREE</span></li><li><span>PARABEN FREE</span></li></ul>
    <p class="hair-types">ALL HAIR TYPES</p>
    <p class="volume">16 Oz / 473 ml</p>
  </div>
</section>

<section class="label label--orange-sham">
  <div class="label__content">
    <div class="brand">Lumi Bright<br>Locks</div>
    <h2 class="title title--big">SHAMPOO</h2>
    <ul class="features"><li>HYDRATING AND MOISTURIZING</li><li>IMPROVES HEALTHY SHINE</li><li>STRENGTHENS HAIR</li><li>ORGANIC INGREDIENTS</li><li>SULFATE FREE</li><li>PARABEN FREE</li></ul>
    <p class="hair-types">ALL HAIR TYPES</p>
    <p class="volume">16 Oz / 473 ml</p>
  </div>
</section>

<section class="label label--leaf-sham">
  <div class="label__panel label__panel--inset" role="img" aria-label="Wavy line pattern in pale yellow and green"></div>
  <div class="label__content">
    <div class="brand">Lumi Bright<br>Locks</div>
    <h2 class="title">SHAMPOO</h2>
    <ul class="features features--loose features--stagger"><li>HYDRATING AND MOISTURIZING</li><li>IMPROVES HEALTHY SHINE</li><li>STRENGTHENS HAIR</li><li>ORGANIC INGREDIENTS</li><li>SULFATE FREE</li><li>PARABEN FREE</li></ul>
    <p class="hair-types">ALL HAIR TYPES</p>
    <p class="volume">16 Oz / 473 ml</p>
  </div>
</section>

<section class="label label--white-sham">
  <div class="label__content">
    <div class="brand">Lumi Bright<br>Locks</div>
    <h2 class="title title--big">SHAMPOO</h2>
    <ul class="features features--stagger"><li>HYDRATING AND MOISTURIZING</li><li>IMPROVES HEALTHY SHINE</li><li>STRENGTHENS HAIR</li><li>ORGANIC INGREDIENTS</li><li>SULFATE FREE</li><li>PARABEN FREE</li></ul>
    <p class="hair-types">ALL HAIR TYPES</p>
    <p class="volume">16 Oz / 473 ml</p>
  </div>
</section>

<aside class="stage">
  <section class="label label--hero">
    <div class="label__content">
      <div class="brand">Lumi Bright<br>Locks</div>
      <h2 class="title">CONDITIONER</h2>
      <ul class="features"><li>HYDRATING AND MOISTURIZING</li><li>IMPROVES HEALTHY SHINE</li><li>STRENGTHENS HAIR</li><li>ORGANIC INGREDIENTS</li><li>SULFATE FREE</li><li>PARABEN FREE</li></ul>
      <p class="hair-types">ALL HAIR TYPES</p>
      <p class="volume">16 Oz / 473 ml</p>
    </div>
  </section>
</aside>

</body>
</html>
```